New Business Card Design Project VORASTI-Italy

we are VORASTI-Italy
our company in the market for 3 years we are luxury cosmetic company and its about time for a facelift :)
i will like to have elegant luxurious and unique business card
that will give the person that get it a unique, luxurious and elegant impression
I'm VERY OPEN FOR NEW IDEAS , even duo i add a few files of things that i see on line and i like them

i add my logo as well
my website is VORASTI.COM
(if you would like to see the main style that we have)

Target Market(s)

adult that have money :)

Industry/Entity Type

Business

Contact Information for Business Card

Name - Paul Vorasti
Position - CEO and CO Founder
address - 4817 E Larkdale
telephone - 555-384-1962
email - paul@vorasti.com
fax - 555-384-1962
website - VORASTI.COM

Colors
000000
959595
fbee3e
ffffff

Requirements
Must have
• big logo in GOLD color
• elegant look
• impressive
Nice to have
• not must but maybe classy pattern background
• not must but maybe emblem
• maybe clear plastic business card
Should not have
• colors
• images

```html
<!DOCTYPE html>
<html lang="en">
<head>
<meta charset="utf-8">
<title>VORASTI Italy – Business Card</title>
<link rel="stylesheet" href="https://fonts.googleapis.com/css2?family=Roboto+Slab:wght@400&family=Tinos&display=swap">
<style>
  :root {
    --canvas: #ffffff;
    --paper: #e8ebed;
    --ink: #4a4a4a;
    --gold: #c49b2e;
  }
  * { margin: 0; padding: 0; box-sizing: border-box; }
  html, body { width: 1200px; height: 1200px; overflow: hidden; background: var(--canvas); }
  .canvas { position: relative; width: 1200px; height: 1200px; }

  .card {
    position: absolute;
    left: 149px;
    width: 909px;
    height: 519px;
    background: linear-gradient(135deg, #eceff1 0%, var(--paper) 55%, #e3e6e8 100%);
  }
  .card--front { top: 48px; }
  .card--back { top: 639px; }

  .contact { font-family: "Roboto Slab", Georgia, serif; color: var(--ink); }
  .contact__line { position: absolute; left: 18px; white-space: nowrap; line-height: 1; }
  .contact__name { top: 65px; font-size: 35px; }
  .contact__role { top: 108px; left: 20px; font-size: 17px; }
  .contact__label { font-size: 27px; }
  .contact__value { font-size: 21px; left: 20px; }

  .brand { position: absolute; text-align: center; font-family: "Tinos", "Times New Roman", serif; font-weight: 400; }
  .brand__mark { position: absolute; border-radius: 50%; }
  .brand__name { position: absolute; white-space: nowrap; line-height: 1; transform: translateX(-50%); }
  .brand__rule { position: absolute; height: 3px; }
  .brand__place { position: absolute; white-space: nowrap; line-height: 1; transform: translateX(-50%); }

  .brand--ink { color: var(--ink); }
  .brand--ink .brand__mark { border: 4px solid var(--ink); }
  .brand--ink .brand__rule { background: var(--ink); }

  .brand--gold { color: var(--gold); }
  .brand--gold .brand__mark { border: 5px solid var(--gold); }
  .brand--gold .brand__rule { background: var(--gold); height: 4px; }
</style>
</head>
<body>
<main class="canvas">

  <section class="card card--front" role="img" aria-label="Business card front on light grey textured paper">
    <div class="contact">
      <p class="contact__line contact__name">Paul Vorasti</p>
      <p class="contact__line contact__role">CEO and CO Founde</p>
      <p class="contact__line contact__label" style="top:181px;">Address</p>
      <p class="contact__line contact__value" style="top:219px;">4817 E Larkdale</p>
      <p class="contact__line contact__label" style="top:254px;">Telephone &amp; Fax</p>
      <p class="contact__line contact__value" style="top:294px;">555-384-1962</p>
      <p class="contact__line contact__label" style="top:324px;">Contact Email</p>
      <p class="contact__line contact__value" style="top:368px;">paul@vorasti.com</p>
      <p class="contact__line contact__label" style="top:400px;left:21px;">Website</p>
      <p class="contact__line contact__value" style="top:443px;left:21px;">www.vorasti.com</p>
    </div>

    <div class="brand brand--ink">
      <span class="brand__mark" style="left:608px;top:93px;width:170px;height:170px;"></span>
      <span class="brand__name" style="left:693px;top:306px;font-size:78px;">VORASTI</span>
      <span class="brand__rule" style="left:502px;top:386px;width:381px;"></span>
      <span class="brand__place" style="left:693px;top:405px;font-size:31px;">ITALY</span>
    </div>
  </section>

  <section class="card card--back" role="img" aria-label="Business card back on light grey textured paper">
    <div class="brand brand--gold">
      <span class="brand__mark" style="left:340px;top:34px;width:230px;height:230px;"></span>
      <span class="brand__name" style="left:455px;top:322px;font-size:106px;">VORASTI</span>
      <span class="brand__rule" style="left:197px;top:431px;width:515px;"></span>
      <span class="brand__place" style="left:455px;top:455px;font-size:42px;">ITALY</span>
    </div>
  </section>

</main>
</body>
</html>
```